energy rating company

Web Design graphics and layout only

To create two pages for the website. First the home page and the second is the design for the job board for our clients use after login. I have attached files that explain in detail what the pages should have and the purpose/desires of each object. Please read these thoroughly.

The webpages need to be clean, professional, easy on the eye, obvious in all its buttons and functions with a strong call to action on the home page and branding and clean, great and obvious looking buttons and very simple but dynamic as well. We wish to be seen as contemporary.

Business Concept

Our business concept is simple, to build a website whereby our clients will be able to upload jobs for energy raters to quote on and subsequent complete the work if their quote is selected. To link energy ratings that are required with energy raters via our website. Similarly to the varlo website, jobs will be “advertised” on the job board and raters will select which jobs they wish to quote for.

I have attached a Word document explaining all the parts of the website and another word document showing what we are sort of after and a excel spreadsheet as well. Please read these in conjunction with this brief!
Updates

Dear All

I have submitted with my brief a word doc and excel spreadsheet of the two pages I want created.  However this is not the layout or design I want, I only put it together so that you will need to know what is required on each page.  Feel free to change and redesign it all.

Also the second page does not require the "process" logo or any other menu items except the first five being Home, How it works, About Us, testimonials and Contact us as per the home page.

We also are looking for something very professional and very clean.  It should be very easy to see exactly what you are looking for.

I will also extend the deadline for new designers!!  I am excited to see your talents!!

Thanks

I have increase budget and posted a note saying feel free to change all the details layout etc on my brief just include everything!!! 

Wanting a professional corporate look...

Want a professional corporate look

We have changed our minds and you we no longer require the process to be on the home page.

Thanks

Target Market(s)

Target Market

Home Inspection Companies
Pest Inspection Companies
Residential home buyers/sellers
Real Estate companies

Industry/Entity Type

It Company

Number of Pages Required

1 page

Requirements
Must have
• Colours and Styles

• The website should be mainly white as I believe it is seen as clean and simple with colour from the logos, but can be swayed if it projects the image we are after.

• It should be obvious and process orientated and I do believe symbols, pictures, etc should replace words where possible.

```html
<!DOCTYPE html>
<html lang="en">
<head>
<meta charset="utf-8">
<title>enrata australia – Energy Rating Quotes</title>
<link rel="stylesheet" href="https://fonts.googleapis.com/css2?family=PT+Sans:wght@400;700&family=Comfortaa:wght@400;700&family=Noto+Sans:wght@400;700&display=swap">
<style>
:root{
  --rust:#b5561f;
  --green:#2f9a3c;
  --green-dark:#1f7f1f;
  --lime:#8cc21a;
  --lime-dark:#7aa80e;
  --orange:#f08a12;
  --amber:#fbb030;
  --yellow:#f2e45a;
  --panel:#f1efed;
  --ink:#1b1b1b;
  --muted:#444;
  --date:#e98a10;
  --bg-top:#ffffff;
  --bg-bottom:#eaf1f9;
}
*{box-sizing:border-box;margin:0;padding:0}
html,body{width:1127px;height:1200px;overflow:hidden}
body{position:relative;background:linear-gradient(var(--bg-top),var(--bg-bottom) 60%,#fff 93%);font-family:"Noto Sans",Tahoma,sans-serif;color:var(--ink)}
.top-rule{position:absolute;left:0;top:0;width:100%;height:6px;background:var(--rust)}
.brand{position:absolute;left:62px;top:158px;font-family:"PT Sans",sans-serif;font-weight:700;font-size:58px;color:var(--green);letter-spacing:-1px}
.main-nav{position:absolute;left:430px;top:40px;width:648px;height:59px;border-radius:10px;background:linear-gradient(#3fb13a,var(--green-dark));display:flex;align-items:center;justify-content:space-evenly;font-family:"PT Sans",sans-serif;font-size:17px;color:#fff}
.main-nav span.sep{opacity:.9}
.quick{position:absolute;top:107px;width:180px;text-align:center;font-family:"PT Sans",sans-serif;font-size:17px;color:var(--green)}
.quick .icon{display:block;margin:0 auto 10px;width:70px;height:75px;border-radius:8px}
.quick small{display:block;color:var(--orange);font-size:12.5px;font-weight:700;margin-top:-3px}
.banner{position:absolute;left:50px;top:230px;width:1028px;height:248px;border:1px solid #c98a2a;border-radius:12px;background:linear-gradient(#f4e65a,var(--amber))}
.banner-inner{position:absolute;left:27px;top:12px;width:974px;height:208px;border-radius:18px;background:linear-gradient(#f0e35c 0%,#f6d44a 55%,#fbad2e 100%)}
.step{position:absolute;top:12px;width:200px;text-align:center;font-family:"PT Sans",sans-serif;font-size:19px;line-height:20px;color:var(--ink)}
.step .icon{display:block;margin:0 auto 12px;width:110px;height:134px;border-radius:14px}
.content{position:absolute;left:50px;top:495px;width:780px;height:610px;border-radius:14px;background:var(--panel);padding:20px 32px}
.welcome{font-size:14px;display:flex;align-items:baseline;gap:6px}
.welcome b{font-family:"Comfortaa",sans-serif;font-weight:700;font-size:31px;color:var(--rust)}
.intro{display:flex;gap:13px;margin-top:12px}
.photo{flex:none;width:268px;height:126px;border-radius:10px;border:2px solid #555;background:linear-gradient(90deg,#b9a58f,#e6d7c4 45%,#c9d4dc)}
.intro p{font-size:12.3px;line-height:20px;margin-bottom:20px}
.tagline{font-family:"PT Sans",sans-serif;font-size:18px;color:var(--rust);margin:12px 0 18px}
.body-text{font-size:12.3px;line-height:20px}
.benefits{list-style:none;margin:16px 0 22px 22px;font-size:12.3px;line-height:20.3px}
.benefits li{position:relative;padding-left:18px}
.benefits li::before{content:"";position:absolute;left:0;top:6px;width:7px;height:7px;border:1.6px solid #222;border-radius:50%;background:radial-gradient(#222 30%,transparent 35%)}
.btn{display:inline-block;font-size:12px;padding:4px 11px;border:1px solid #c67b11;background:linear-gradient(#fbd36a,var(--orange));color:#222}
.content .btn{position:absolute;right:22px;bottom:14px}
.signin{position:absolute;left:846px;top:495px;width:232px;height:203px;border-radius:10px;overflow:hidden;background:var(--lime)}
.box-head{height:37px;padding:7px 16px;font-family:"PT Sans",sans-serif;font-size:19px;color:#fff;background:var(--lime-dark)}
.signin form{padding:10px 17px}
.signin input{display:block;width:197px;height:20px;border:1px solid #6a9a10;margin:0 0 12px;padding:0 5px;font-size:11.5px;color:#999;font-family:inherit}
.signin .btn{margin:2px 0 10px;font-size:12px}
.signin .help{font-size:12px}
.signin .join{position:absolute;left:0;bottom:0;width:100%;height:36px;background:var(--lime-dark);padding:9px 12px;font-size:12px;text-align:right}
.join b{color:#fff;font-size:14px}.join strong{font-size:15px}
.testimonials{position:absolute;left:846px;top:718px;width:232px;height:387px;border-radius:10px;overflow:hidden;background:#fff}
.testimonials .box-head{background:linear-gradient(#fbd46a,var(--amber));color:#222}
.quote{padding:9px 11px 0 17px}
.quote h4{display:flex;justify-content:space-between;font-size:12.5px;padding-bottom:5px;border-bottom:1px dotted #999}
.quote h4 span{color:var(--date)}
.quote p{font-size:11.8px;line-height:19px;color:var(--muted);margin-top:4px}
.quote a{display:block;text-align:right;font-size:12.5px;font-weight:700;color:var(--lime-dark);text-decoration:none;margin-top:8px}
.more{position:absolute;left:0;bottom:0;width:100%;height:38px;background:var(--lime-dark);color:#fff;font-family:"PT Sans",sans-serif;font-weight:700;font-size:15px;text-align:center;padding-top:9px}
.foot-rule{position:absolute;left:0;top:1122px;width:100%;height:5px;background:var(--rust)}
.foot-nav{position:absolute;top:1144px;width:100%;text-align:center;font-size:12px;word-spacing:2px}
.foot-nav span{margin:0 18px}
.copyright{position:absolute;top:1165px;width:100%;text-align:center;font-size:12px}
</style>
</head>
<body>
<div class="top-rule"></div>
<div class="brand">enrata australia</div>

<nav class="main-nav">
  <span>Home</span><span class="sep">|</span><span>How it works</span><span class="sep">|</span><span>About Us</span><span class="sep">|</span><span>Testimonials</span><span class="sep">|</span><span>Contact Us</span>
</nav>

<div class="quick" style="left:461px"><span class="icon" role="img" aria-label="Pencil icon" style="background:linear-gradient(135deg,#e54a2a,#f7c632 55%,#e8e2d0)"></span>Get A Quote</div>
<div class="quick" style="left:658px"><span class="icon" role="img" aria-label="Bar chart icon" style="background:linear-gradient(90deg,#c0302a,#2b78c8,#f2b51e,#3ea83a)"></span>Energy Raters<small>Add your busines</small></div>
<div class="quick" style="left:855px"><span class="icon" role="img" aria-label="Documents icon" style="background:linear-gradient(#cfe0f2,#8fb0d6)"></span>Active Job Board</div>

<section class="banner">
  <div class="banner-inner">
    <div class="step" style="left:36px"><span class="icon" role="img" aria-label="Businessman illustration" style="background:linear-gradient(#e2763a 30%,#2bb0c8 60%,#1a7f9a)"></span>post a<br>JOB</div>
    <div class="step" style="left:239px"><span class="icon" role="img" aria-label="Checklist with arrow illustration" style="background:linear-gradient(135deg,#f4f6fa,#b9cfe8 60%,#3a8be0)"></span>get as many<br>QUOTES as you like</div>
    <div class="step" style="left:441px"><span class="icon" role="img" aria-label="Newspaper and folder illustration" style="background:linear-gradient(135deg,#e4b64e,#ece7dc 50%,#9aa6b4)"></span>select ENERGY<br>QUOTE that suits</div>
    <div class="step" style="left:644px"><span class="icon" role="img" aria-label="Signed contract with pen illustration" style="background:linear-gradient(135deg,#a9c0e0,#eef2f8 55%,#d24a3a)"></span>approve<br>PAYMENT</div>
    <div class="step" style="left:846px"><span class="icon" role="img" aria-label="Database cylinder illustration" style="background:linear-gradient(#f2f2f2 25%,#1e7fd0 45%,#7cc0f0 70%,#1a66b0)"></span>receive<br>RATING</div>
  </div>
</section>

<main class="content">
  <h1 class="welcome">Welcome To <b>enrata australia</b></h1>
  <div class="intro">
    <div class="photo" role="img" aria-label="Photo of a smiling team of consultants"></div>
    <div>
      <p><strong>enrata australia</strong> is Australia's leading professional energy rating consultancy firm specializing in large scaled residential and commercial energy rating logistics.</p>
      <p>We have professional and accredited energy raters in all States and Territories ready and waiting to provide quotes for and perform&nbsp; your energy rating jobs!</p>
    </div>
  </div>
  <h2 class="tagline">It's Free, Fast and Easy to use and you get the best price and turnaround time that suits you!!</h2>
  <p class="body-text">Register with us, upload your job and specifications, and sit back and watch as energy raters provide quotes for your work!</p>
  <ul class="benefits">
    <li>Get the best priced quotes for your energy ratings</li>
    <li>Save time by listing a job to get many quotes</li>
    <li>Monitor your jobs and quotes on your own job board</li>
    <li>Be notified via email of all new quotes as they come in</li>
    <li>Be able to specify your desired turnaround times</li>
    <li>Accessible anytime and anywhere</li>
    <li>Choose a deadline for energy raters to supply quotes</li>
    <li>Have access to many qualified energy raters in your state all quoting for your work</li>
    <li>Be able to track your jobs and pay online</li>
    <li>Provide feedback on energy raters</li>
  </ul>
  <p class="body-text">Its totally free to be registered with us and there is no obligations or hidden catches!&nbsp; So if you wish to utilise the amazing opportunity register now!&nbsp; This new website will be going live on the (insert date) so be ready to save some</p>
  <a class="btn">read more.</a>
</main>

<aside class="signin">
  <div class="box-head">Sign in</div>
  <form>
    <input type="text" placeholder="user id">
    <input type="password" placeholder="password">
    <a class="btn">sign in</a>
    <p class="help">can't access your account?</p>
  </form>
  <div class="join">New to <b>enrata australia?</b> <strong>sign up</strong></div>
</aside>

<aside class="testimonials">
  <div class="box-head">Testimonials</div>
  <div class="quote"><h4>Ian Hale <span>22-03-2010</span></h4><p>Lorem Ipsum is simply dummy text of the printing and typesetting industry.</p><a>read more</a></div>
  <div class="quote"><h4>Robin Marsh <span>18-03-2010</span></h4><p>Vestibulum eget erat in nulla aliquam malesuada id a nunc.</p><a>read more</a></div>
  <div class="quote"><h4>Jasmin <span>22-03-2010</span></h4><p>Lorem Ipsum is simply dummy text of the printing and typesetting industry.</p><a>read more</a></div>
  <div class="more">view more testimonials</div>
</aside>

<div class="foot-rule"></div>
<nav class="foot-nav"><span>Home</span>|<span>How it works</span>|<span>About Us</span>|<span>Testimonials</span>|<span>Contact Us</span></nav>
<p class="copyright">copyright reserved, 2010 - 2011, enrata australia</p>
</body>
</html>
```